Briefbogen und Visitenkarte für Grundstücksverwaltunggesellschaft
Zielgruppe
Wir sind eine Grundstücksverwaltungsgesellschaft und Verwalten eine Vielzahl an Logistik- und Industrieimmobilien.
Aufgabenstellung
Wir bitten um Verwendung unseres Logo, siehe Anlage. Die Bildmarke darf nicht verändert werden, die Wortmarke darf unter Umständen otimiert werden.
Wir möchten einen dezenten Auftritt vermitteln und bitten daher um graue Schrift als Grundfarbe.
Bei der Visitenkarte könnten wir uns eine einfarbig blaue Rückseite vorstellen.
Folgende Daten kommen zur Verwendung:
Lindwerk Grundstücksverwaltungs GmbH
Internet: www.lindwerk-grundbesitz.de

```html
<!DOCTYPE html>
<html lang="de">
<head>
<meta charset="utf-8">
<title>Lindwerk Grundstücksverwaltungs GmbH – Geschäftsausstattung</title>
<link href="https://fonts.googleapis.com/css2?family=Jura:wght@400;500&display=swap" rel="stylesheet">
<style>
  :root{
    --bg:#f7f7f7;
    --paper:#ffffff;
    --grey:#8a8a8a;
    --grey-dark:#5e5e5e;
    --grey-light:#b5b5b5;
    --blue:#00507f;
  }
  *{margin:0;padding:0;box-sizing:border-box}
  html,body{width:1200px;height:1000px;overflow:hidden;background:var(--bg)}
  body{position:relative;font-family:"Jura",sans-serif;color:var(--grey)}
  .sheets{position:absolute;left:0;top:0;width:1200px;height:1000px}
  .abs{position:absolute;white-space:nowrap}
  .mark{position:absolute;background:var(--grey)}
  .wordmark{position:absolute;white-space:nowrap;letter-spacing:.08em;color:var(--grey);font-weight:500}
  .contact{position:absolute;line-height:1.3}
  .contact .label{display:inline-block;color:var(--grey-dark)}
  .contact .row{font-size:5px;color:var(--grey)}
  .contact .row .label{font-size:6.4px}
  .contact .title{font-size:6.6px;color:var(--grey-dark);margin-bottom:1px}
  .contact .company{font-size:6.4px;color:var(--grey-dark);margin-top:4px}
  .contact .addr{font-size:5px}
  .footer-line{position:absolute;left:29px;width:533px;text-align:center;font-size:5px;color:var(--grey)}
  .footer-line .label{font-size:6.2px}
  .address{position:absolute;left:685px;top:336px;font-size:7.5px;line-height:11.7px;color:var(--grey-dark)}
  .flap-text{position:absolute;width:200px;text-align:center;font-size:5px;color:var(--grey-dark)}
  .flap-text small{display:block;font-size:4px;color:var(--grey)}
</style>
</head>
<body>

<svg class="sheets" width="1200" height="1000" viewBox="0 0 1200 1000" aria-hidden="true">
  <defs>
    <filter id="shadow" x="-5%" y="-5%" width="112%" height="115%">
      <feDropShadow dx="2" dy="3" stdDeviation="2" flood-color="#000" flood-opacity=".28"/>
    </filter>
  </defs>

  <!-- letterhead -->
  <g class="letterhead">
    <rect x="29" y="111" width="533" height="754" fill="var(--paper)" filter="url(#shadow)"/>
    <line x1="393" y1="111" x2="393" y2="265" stroke="var(--grey)" stroke-width=".7"/>
    <rect x="541" y="153" width="21" height="31" fill="var(--grey)"/>
    <line x1="29" y1="374" x2="50" y2="374" stroke="var(--grey)" stroke-width=".8"/>
    <line x1="29" y1="612" x2="50" y2="612" stroke="var(--grey)" stroke-width=".8"/>
    <rect x="218" y="854" width="153" height="9" fill="var(--grey-light)"/>
  </g>

  <!-- envelope front -->
  <g class="envelope-front">
    <rect x="609" y="161" width="546" height="280" fill="var(--paper)" filter="url(#shadow)"/>
    <path d="M609 161 L636 80 Q639 74 646 74 L1117 74 Q1123 74 1126 80 L1155 161 Z" fill="var(--paper)" stroke="#e2e2e2" stroke-width=".6"/>
    <line x1="609" y1="161" x2="1155" y2="161" stroke="#d0d0d0" stroke-width=".8"/>
    <rect x="642" y="318" width="219" height="88" rx="11" fill="var(--paper)" stroke="#c8c8c8" stroke-width="1"/>
  </g>

  <!-- envelope back -->
  <g class="envelope-back">
    <rect x="611" y="464" width="547" height="281" fill="var(--paper)" filter="url(#shadow)"/>
    <path d="M612 465 L637 542 Q640 551 650 551 L1122 551 Q1131 551 1134 542 L1157 465" fill="none" stroke="#d8d8d8" stroke-width="1"/>
  </g>

  <!-- business card front -->
  <g class="card-front">
    <rect x="603" y="809" width="257" height="151" fill="var(--paper)" filter="url(#shadow)"/>
    <rect x="807" y="809" width="4.6" height="41" fill="var(--grey)"/>
    <rect x="807" y="913" width="4.6" height="47" fill="var(--grey)"/>
  </g>

  <!-- business card back -->
  <rect class="card-back" x="869" y="809" width="257" height="151" fill="var(--blue)" filter="url(#shadow)"/>
</svg>

<!-- letterhead content -->
<div class="mark" style="left:61px;top:156px;width:14px;height:14px"></div>
<div class="wordmark" style="left:82px;top:154px;font-size:11.5px">Lindwerk Grundstücksverwaltungs GmbH</div>

<div class="contact" style="left:402px;top:131px">
  <div class="title">Kontakt</div>
  <div class="row"><span class="label" style="width:19px">Tel.</span>0451 482170-0</div>
  <div class="row"><span class="label" style="width:19px">Fax</span>0451 482170-33</div>
  <div class="row"><span class="label" style="width:19px">Mobil</span>0174 6253408 (nur auf VK)</div>
  <div class="row"><span class="label" style="width:19px">E-mai</span>info@lindwerk-grundbesitz.de</div>
  <div class="row"><span class="label" style="width:19px">Web</span>www.lindwerk-grundbesitz.de</div>
  <div class="company">Lindwerk Grundstücksverwaltungs GmbH</div>
  <div class="addr">Kornmesserweg 9</div>
  <div class="addr">23562 Lübeck</div>
</div>

<div class="footer-line" style="top:829px"><span class="label">Bankverbindung:</span> Nordbank Hanse AG • IBAN: DE00 2100 4400 0004 4172 05 • BIC: NBHADE2HXXX</div>
<div class="footer-line" style="top:840px">USt.IDNr.: DE319274058 • Steuernummer: 22 417 30916 • Amtsgericht Lübeck, HRB 4187 HL</div>

<!-- envelope front content -->
<div class="flap-text" style="left:782px;top:92px;transform:rotate(180deg)">Lindwerk Grundstücksverwaltungs GmbH<small>Kornmesserweg 9 | 23562 Lübeck</small></div>
<div class="mark" style="left:875px;top:114px;width:14px;height:14px"></div>
<div class="mark" style="left:654px;top:210px;width:14px;height:14px"></div>
<div class="wordmark" style="left:675px;top:208px;font-size:11.5px">Lindwerk Grundstücksverwaltungs GmbH</div>
<div class="address">
  Clara Wendt<br>
  Am Lindenhang 12<br>
  53721 Siegburg<br>
  SCHWEIZ
</div>

<!-- envelope back content -->
<div class="mark" style="left:877px;top:490px;width:14px;height:14px"></div>
<div class="flap-text" style="left:784px;top:520px">Lindwerk Grundstücksverwaltungs GmbH<small>Kornmesserweg 9 | 23562 Lübeck</small></div>

<!-- business card front content -->
<div class="abs" style="left:623px;top:831px;font-size:8.6px;color:var(--grey-dark)">Jonas Feldmann</div>
<div class="abs" style="left:623px;top:842px;font-size:6.4px;color:var(--grey)">Geschäftsführer</div>
<div class="contact" style="left:624px;top:859px">
  <div class="title">Kontakt</div>
  <div class="row"><span class="label" style="width:19px">Tel.</span>0451 482170-0</div>
  <div class="row"><span class="label" style="width:19px">Fax</span>0451 482170-33</div>
  <div class="row"><span class="label" style="width:19px">Mobil</span>0174 6253408 (nur auf VK)</div>
  <div class="row"><span class="label" style="width:19px">E-mai</span>info@lindwerk-grundbesitz.de</div>
  <div class="row"><span class="label" style="width:19px">Web</span>www.lindwerk-grundbesitz.de</div>
  <div class="company">Lindwerk Grundstücksverwaltungs GmbH</div>
  <div class="addr">Kornmesserweg 9</div>
  <div class="addr">23562 Lübeck</div>
</div>

<!-- business card back content -->
<div class="mark" style="left:885px;top:879px;width:12px;height:12px;background:#fff"></div>
<div class="wordmark" style="left:903px;top:878px;font-size:8.6px;color:#fff">Lindwerk Grundstücksverwaltungs GmbH</div>

</body>
</html>
```